Dental Office Business Card

We need a business card for our pediatric dentistry office.
On one side the design needs to contain the following:
our logo (attached)
Vento Pediatric Grins
Soraya Kadbelani, DDS
Board Certified Pediatric Dentist
Tel: (555) 318-2747)
Fax: (555) 264-8031
Email: info@ventopediatricgrins.example
Web: www.ventopediatricgrins.example
Address: 41 Brindle Ave, Suite 208, Wellesley, MA 02099

On the other side of the card, the design needs to have an appointment reminder (date and time as well as day of the week) similar to the design attached (no need for appointment reason “For”)

```html
<!DOCTYPE html>
<html lang="en">
<head>
<meta charset="utf-8">
<title>Vento Pediatric Grins – Business Card</title>
<link href="https://fonts.googleapis.com/css2?family=Lato:wght@400;700;900&display=swap" rel="stylesheet">
<style>
  :root {
    --backdrop: #8e8e8e;
    --card: #ffffff;
    --ink: #1e1e1e;
    --text: #2b2b2b;
    --mint: #a6dbae;
    --mint-deep: #8fd19b;
    --dots: #555555;
  }
  * { box-sizing: border-box; margin: 0; padding: 0; }
  html, body { width: 1200px; height: 1200px; overflow: hidden; }
  body {
    background: var(--backdrop);
    font-family: "Lato", Arial, sans-serif;
    color: var(--text);
    position: relative;
  }
  .card {
    position: absolute;
    left: 250px;
    width: 700px;
    height: 400px;
    background: var(--card);
    border-radius: 20px;
    overflow: hidden;
    box-shadow: 0 3px 8px rgba(0,0,0,0.25);
  }
  .card--front { top: 170px; }
  .card--back { top: 631px; }

  /* Front */
  .brand {
    position: absolute;
    right: 41px;
    top: 62px;
    display: flex;
    align-items: center;
    gap: 14px;
  }
  .brand__dot {
    width: 44px; height: 44px;
    border-radius: 50%;
    background: var(--mint);
  }
  .brand__name {
    font-weight: 900;
    color: var(--ink);
    font-size: 44px;
    line-height: 1;
    text-align: right;
  }
  .brand__name span { display: block; }
  .brand__name .brand__sub { font-size: 22px; letter-spacing: 0.4px; margin-top: 6px; }

  .person { position: absolute; left: 38px; top: 193px; }
  .person__name {
    font-weight: 900;
    font-size: 23px;
    color: var(--ink);
    letter-spacing: -0.2px;
  }
  .person__title {
    font-size: 16px;
    color: var(--mint-deep);
    letter-spacing: 0.2px;
  }
  .divider {
    position: absolute;
    left: 40px; right: 41px; top: 254px;
    height: 1px; background: var(--ink);
  }
  .contacts {
    position: absolute; left: 39px; top: 271px;
    list-style: none;
    font-size: 16px;
    letter-spacing: 0.3px;
  }
  .contacts li { display: flex; align-items: center; height: 24.5px; }
  .contacts svg { width: 13px; height: 13px; margin-right: 13px; fill: var(--mint); }
  .address {
    position: absolute; right: 41px; top: 271px;
    text-align: right; font-size: 16px; line-height: 24.5px; letter-spacing: 0.3px;
    font-style: normal;
  }
  .address__company { color: var(--mint-deep); font-weight: 700; }
  .footer-band { position: absolute; left: 0; bottom: 0; width: 700px; height: 40px; }
  .website {
    position: absolute; right: 41px; bottom: 9px;
    color: #fff; font-size: 16px; letter-spacing: 0.4px;
  }

  /* Back */
  .appt__title {
    position: absolute; top: 45px; width: 100%;
    text-align: center; font-weight: 900; font-size: 31px;
    color: var(--ink); letter-spacing: 0.3px;
  }
  .field {
    position: absolute; display: flex; align-items: baseline;
    font-size: 17px; color: var(--ink);
  }
  .field__fill { flex: 1; border-bottom: 1.3px dotted var(--dots); margin: 0 1px; transform: translateY(-2px); }
  .field--name { left: 52px; right: 59px; top: 117px; }
  .field--date { left: 52px; width: 297px; top: 170px; }
  .field--time { left: 349px; right: 59px; top: 170px; }
  .field__suffix { font-size: 13px; }
  .days {
    position: absolute; top: 244px; left: 112px;
    display: flex; list-style: none; font-size: 17px; color: var(--ink);
  }
  .days li { display: flex; align-items: center; margin-right: 25px; }
  .days li:last-child { margin-right: 0; }
  .days .box {
    width: 15px; height: 15px; border: 1.6px solid var(--mint);
    margin-right: 7px;
  }
  .notice {
    position: absolute; top: 324px; width: 100%;
    text-align: center; font-size: 13.5px; line-height: 17.5px; color: var(--ink);
  }
</style>
</head>
<body>

<section class="card card--front">
  <div class="brand">
    <div class="brand__dot"></div>
    <div class="brand__name"><span>Vento</span><span class="brand__sub">PEDIATRIC GRINS</span></div>
  </div>

  <div class="person">
    <h1 class="person__name">SORAYA KADBELANI, DDS</h1>
    <p class="person__title">Board Certified Pediatric Dentist</p>
  </div>

  <div class="divider"></div>

  <ul class="contacts">
    <li><svg viewBox="0 0 24 24"><path d="M6.6 10.8a15.1 15.1 0 0 0 6.6 6.6l2.2-2.2a1 1 0 0 1 1-.25 11.4 11.4 0 0 0 3.6.57 1 1 0 0 1 1 1V20a1 1 0 0 1-1 1A17 17 0 0 1 3 4a1 1 0 0 1 1-1h3.5a1 1 0 0 1 1 1c0 1.250.2 2.450.57 3.57a1 1 0 0 1-.25 1z"/></svg>(555) 318-2747</li>
    <li><svg viewBox="0 0 24 24"><path d="M6 2h10l2 2v4H6zM3 9h18a1 1 0 0 1 1 1v7h-4v5H6v-5H2v-7a1 1 0 0 1 1-1zm5 8v3h8v-3z"/></svg>(555) 264-8031</li>
    <li><svg viewBox="0 0 24 24"><path d="M2 5h20v14H2zm2 2v.4l8 5.2 8-5.2V7z"/></svg>info@ventopediatricgrins.example</li>
  </ul>

  <address class="address">
    <div class="address__company">Vento Pediatric Grins</div>
    <div>41 Brindle Ave, Suite 208</div>
    <div>Ashbrook Glen, MA 02099</div>
  </address>

  <svg class="footer-band" viewBox="0 360 700 40" preserveAspectRatio="none">
    <path d="M0 375 H388 C378 377 372 385 355 385 H0 Z" fill="#a6dbae"/>
    <path d="M0 390 H360 C382 390 386 363 412 363 H700 V400 H0 Z" fill="#1e1e1e"/>
  </svg>
  <div class="website">www.ventopediatricgrins.example</div>
</section>

<section class="card card--back">
  <h2 class="appt__title">NEXT APPOINTMENT</h2>

  <div class="field field--name"><span>NAME</span><span class="field__fill"></span></div>
  <div class="field field--date"><span>DATE</span><span class="field__fill"></span></div>
  <div class="field field--time"><span>TIME</span><span class="field__fill"></span><span class="field__suffix">AM\PM</span></div>

  <ul class="days">
    <li><span class="box"></span>MON</li>
    <li><span class="box"></span>TUES</li>
    <li><span class="box"></span>WED</li>
    <li><span class="box"></span>THU</li>
    <li><span class="box"></span>FRI</li>
    <li><span class="box"></span>SAT</li>
  </ul>

  <p class="notice">If you are unable to keep your appointment, please call us to<br>rescheduleatleast 48 hours prior to your appointment.</p>
</section>

</body>
</html>
```